Online Art Gallery & Art Management Firm looking for a business card

I'm launching an online art gallery (paintings, photography, drawings, furniture, books, ...) where people can buy all types of art. It's a platform where young and unknown artists can showcase their oeuvre.

Additionally, the venture will act as my advising company for artists. I help them out with their business side of life and become their representative.

The company name: The Velvet Parlour
Logo is attached

I'm looking for something very classy and upmarket.
Updates

Reason: Logo wasn't finished yet...

The design should include the following information: - Name: Pieter Vandomme - Title: Founder - Mobile: +32 (0) 486 514 362 - E-mail: pieter@velvet-parlour.example - Website www.velvet-parlour.example I prefer the have the logo (without website) on the one side and the information on the other. Best regards Pieter

Target Market(s)

Art buyers / art dealers / artists / middle class / upmarket /

Industry/Entity Type

Artists

Colors

Designer to choose colors to be used in the design.

Requirements
Must have
• Must communicate credibility, trust and integrity
Nice to have
• Something classy, chique
Should not have
• Nothing to artistic or creative

```html
<!DOCTYPE html>
<html lang="en">
<head>
<meta charset="utf-8">
<title>The Velvet Parlour – Business Card</title>
<link rel="stylesheet" href="https://fonts.googleapis.com/css2?family=Jost:wght@300;400&display=swap">
<style>
  :root {
    --backdrop: #2a2a2a;
    --card: #060606;
    --copper: #a86a3c;
    --ink-light: #e6e6e6;
  }
  * { margin: 0; padding: 0; box-sizing: border-box; }
  html, body {
    width: 1200px;
    height: 1000px;
    overflow: hidden;
    background: var(--backdrop);
    font-family: "Jost", "Helvetica Neue", Arial, sans-serif;
  }
  .card {
    position: absolute;
    left: 300px;
    width: 600px;
    height: 380px;
    background: var(--card);
    box-shadow: 0 6px 18px rgba(0,0,0,.45);
  }
  .card--front { top: 80px; }
  .card--back  { top: 520px; }

  .wordmark {
    color: var(--copper);
    font-weight: 300;
    text-transform: uppercase;
    white-space: nowrap;
    line-height: 1;
  }
  .card--front .wordmark {
    position: absolute;
    left: 0; right: 0;
    top: 50%;
    transform: translateY(-50%);
    text-align: center;
    font-size: 28px;
    letter-spacing: 0.2em;
  }

  /* Back: brand line — name left, wordmark right, both above the rule */
  .card--back .wordmark {
    position: absolute;
    right: 186px;
    top: 94px;
    font-size: 17px;
    letter-spacing: 0.18em;
  }
  .divider {
    position: absolute;
    left: 40px;
    top: 120px;
    width: 375px;
    height: 1px;
    background: var(--copper);
  }
  .website {
    position: absolute;
    right: 40px;
    top: 113px;
    font-size: 11px;
    line-height: 1.3;
    font-weight: 400;
    color: var(--copper);
    white-space: nowrap;
  }
  .person {
    position: absolute;
    left: 40px;
    top: 82px;
  }
  .person__name {
    color: var(--ink-light);
    font-size: 15px;
    font-weight: 400;
    line-height: 1.1;
    white-space: nowrap;
  }
  .person__title,
  .contact__label {
    color: var(--copper);
    font-size: 10px;
    font-weight: 300;
    line-height: 1.3;
  }
  .contact {
    position: absolute;
    left: 40px;
    bottom: 40px;
    list-style: none;
  }
  .contact__item + .contact__item { margin-top: 12px; }
  .contact__value {
    color: var(--ink-light);
    font-size: 13px;
    font-weight: 400;
    line-height: 1.2;
    white-space: nowrap;
  }
</style>
</head>
<body>
  <section class="card card--front" aria-label="Card front">
    <div class="wordmark">The Velvet Parlour</div>
  </section>

  <section class="card card--back" aria-label="Card back">
    <div class="person">
      <div class="person__name">Pieter Vandomme</div>
      <div class="person__title">Founder</div>
    </div>
    <div class="wordmark">The Velvet Parlour</div>
    <div class="divider"></div>
    <div class="website">www.velvet-parlour.example</div>

    <ul class="contact">
      <li class="contact__item">
        <div class="contact__value">+32 (0) 486 514 362</div>
        <div class="contact__label">Mobile</div>
      </li>
      <li class="contact__item">
        <div class="contact__value">pieter@velvet-parlour.example</div>
        <div class="contact__label">E-mail</div>
      </li>
    </ul>
  </section>
</body>
</html>
```